Biz Cards for Velmora Associates

Velmora Associates is seeking a single-sided business card that is more visually-appealing than our current design (see attached).

Notes:
- Our colors are blue & teal.
- Our tag line must be large enough to be easily read
- We don't necessarily need our address included (that's just the biz office)
- We'd like to add our email address: Velmora417@quillbox.net

Thanks!

Industry/Entity Type

Business

Contact Information for Business Card

Standard size
PSD file required w/ text on its own layer

Colors
86cfc6
3277b5

```html
<!DOCTYPE html>
<html lang="en">
<head>
<meta charset="utf-8">
<title>Velmora Associates – Business Card</title>
<link href="https://fonts.googleapis.com/css2?family=Roboto:wght@400;500;700&display=swap" rel="stylesheet">
<style>
  :root {
    --brand-blue: #2f77c0;
    --brand-teal: #86cfc6;
    --ink: #1c1c1c;
    --muted: #4a4a4a;
    --card: #ffffff;
    --backdrop: #e9ebee;
  }
  * { margin: 0; padding: 0; box-sizing: border-box; }
  html, body { width: 1200px; height: 801px; overflow: hidden; }
  body {
    background: var(--backdrop);
    font-family: "Roboto", Arial, sans-serif;
    display: flex; align-items: center; justify-content: center;
  }
  .business-card {
    position: relative;
    width: 700px; height: 400px;
    background: var(--card);
    box-shadow: 0 6px 24px rgba(0,0,0,0.12);
    overflow: hidden;
  }
  .brand {
    position: absolute; left: 40px; top: 118px; width: 300px;
    display: flex; align-items: center; gap: 14px;
  }
  .brand-dot {
    width: 30px; height: 30px; border-radius: 50%;
    background: var(--brand-teal); flex: none;
  }
  .brand-name {
    font-size: 28px; font-weight: 500; color: var(--ink);
    line-height: 1.15; letter-spacing: 0.5px;
  }
  .divider {
    position: absolute; left: 380px; top: 40px;
    width: 3px; height: 145px; background: var(--brand-blue);
  }
  .contact {
    position: absolute; left: 408px; top: 30px;
  }
  .person-name {
    font-size: 22px; font-weight: 700; color: var(--brand-blue);
  }
  .person-role {
    font-size: 15px; color: var(--ink); margin-top: 2px; margin-bottom: 18px;
  }
  .contact-list { list-style: none; }
  .contact-list li {
    display: flex; align-items: center; gap: 12px;
    font-size: 15px; color: var(--muted); line-height: 24px;
  }
  .contact-list svg { width: 14px; height: 14px; flex: none; }
  .band-accent {
    position: absolute; left: 0; right: 0; bottom: 78px;
    height: 4px; background: var(--brand-teal);
  }
  .tagline-band {
    position: absolute; left: 0; right: 0; bottom: 0; height: 76px;
    background: var(--brand-blue);
    display: flex; align-items: center; justify-content: center;
    padding-left: 120px;
  }
  .tagline {
    color: #fff; font-size: 20px; font-weight: 500; letter-spacing: 0.2px;
  }
</style>
</head>
<body>
  <div class="business-card">
    <div class="brand">
      <span class="brand-dot"></span>
      <span class="brand-name">Velmora Associates</span>
    </div>

    <div class="divider"></div>

    <div class="contact">
      <div class="person-name">Dana Whitfield, RN</div>
      <div class="person-role">Mental Health Therapist</div>
      <ul class="contact-list">
        <li>
          <svg viewBox="0 0 14 14"><rect x="3.5" y="1" width="7" height="12" rx="1.2" fill="none" stroke="#2f77c0" stroke-width="1.4"/></svg>
          (855) VEL-MORA
        </li>
        <li>
          <svg viewBox="0 0 14 14"><rect x="4" y="1" width="6" height="4" fill="#2f77c0"/><rect x="1" y="5" width="12" height="5" rx="1" fill="#2f77c0"/><rect x="4" y="9" width="6" height="4" fill="#fff" stroke="#2f77c0" stroke-width="1.2"/></svg>
          (330) 555-0182
        </li>
        <li>
          <svg viewBox="0 0 14 14"><rect x="1" y="3" width="12" height="8" fill="#2f77c0"/><path d="M1 3 L7 8 L13 3" fill="none" stroke="#fff" stroke-width="1.2"/></svg>
          Velmora417@quillbox.net
        </li>
        <li>
          <svg viewBox="0 0 14 14"><circle cx="6" cy="6" r="4" fill="none" stroke="#2f77c0" stroke-width="2"/><line x1="9" y1="9" x2="13" y2="13" stroke="#2f77c0" stroke-width="2.2"/></svg>
          VelmoraCare.net
        </li>
      </ul>
    </div>

    <div class="band-accent"></div>
    <div class="tagline-band">
      <span class="tagline">Insightful Minds | Warm Hearts | Great Patients</span>
    </div>
  </div>
</body>
</html>
```